Business Card: RW Office Partners - Your tidy answer finder

Business Name: RW Office Partners
Website: www.rwofficepartners.com.au
Email: marisol@rwofficepartners.com.au
Mobile: 61 487 902 346
Facebook: @rwofficepartners
Instrgram: @rwofficepartners

Brading Colours:
HEX
#986474
#ddccd3
#7a8498
#c9d8e4
#000000
#ffffff

Tag Line: Your organised problem solver

Link to DRAFT website:
https://helpdeskhub.sitebuilderx.com/rw-office-partners

About Page from the website:
My name is Marisol Bramwell, and I would love to assist you to become more productive in your day to day and achieve your business and personal goals.
My mission is to give you time, time to work on the important tasks of your business or to be able to spend more time with your family. I will take on the tasks you don’t have time for, don’t know well or simply don’t like to do.
I have an extensive background in Administration, Tender Coordination, Document Control, WHS and Quality Management working primarily in the Construction, Mining and Corporate World.
I am passionate about being organised, having order and making things in your life (and mine) easier! I love to watch something unfold and grow into something amazing! I am known for being the go-to problem solver, the organiser of all things, producing high standards of work even under pressure. I’m also a confident communicator, and I understand that you’re busy running your business.

Target Market(s)

Small to Medium Business who require assistance in their business by a virtual assistant.

Industry/Entity Type

Virtual Assistant

Contact Information for Business Card

Mobile: 61 487 902 346

Font styles to use
Sans Serif

Colors
ffffff

Requirements
Must have
• Branding Colours as outlined.
Contact Details as outlined.
Logo as provided.
Proper contact details - mobile, facebook, instragm, website.
Simple, Elegant, very clean looking.
Should not have
• Note cute with pictures.
Not too girly as still want to market to construction companies.

```html
<!DOCTYPE html>
<html lang="en">
<head>
<meta charset="utf-8">
<title>RW Office Partners – Business Card</title>
<link rel="stylesheet" href="https://fonts.googleapis.com/css2?family=Lato:wght@400;700&display=swap">
<style>
  :root {
    --rose: #986474;
    --blush: #ddccd3;
    --blush-light: #ebe0e4;
    --slate: #7a8498;
    --mist: #c9d8e4;
    --ink: #1c1c1e;
    --black: #000000;
    --white: #ffffff;
    --backdrop: #e9e6e3;
    --text-dark: #2a2a2c;
  }
  * { box-sizing: border-box; margin: 0; padding: 0; }
  html, body { width: 1200px; height: 1000px; overflow: hidden; }
  body {
    background: var(--backdrop);
    font-family: "Lato", Arial, sans-serif;
    position: relative;
  }
  .card {
    position: absolute;
    left: 250px;
    width: 700px;
    height: 400px;
    background: var(--ink);
    overflow: hidden;
    box-shadow: 0 6px 18px rgba(0,0,0,0.18);
  }
  .card--front { top: 60px; }
  .card--back { top: 520px; }

  .card__art { position: absolute; inset: 0; width: 100%; height: 100%; }

  .wordmark {
    position: absolute;
    font-family: "Lato", Arial, sans-serif;
    font-weight: 700;
    color: var(--mist);
    letter-spacing: 2px;
    text-transform: uppercase;
    text-align: center;
    white-space: nowrap;
  }
  .wordmark__line { display: block; }
  .card--front .wordmark {
    left: 200px; width: 300px; top: 150px;
    font-size: 40px;
    line-height: 1.2;
  }
  .card--back .wordmark {
    left: 400px; width: 280px; top: 128px;
    font-size: 26px;
    line-height: 1.25;
  }

  .contact-list {
    position: absolute;
    left: 34px;
    top: 218px;
    list-style: none;
    color: var(--text-dark);
    font-size: 19px;
  }
  .contact-list li {
    display: flex;
    align-items: center;
    gap: 10px;
    height: 30px;
  }
  .contact-list .icon { width: 20px; height: 20px; flex: none; }
</style>
</head>
<body>

  <section class="card card--front" aria-label="Business card front">
    <svg class="card__art" viewBox="0 0 700 400" aria-hidden="true">
      <g stroke="var(--white)" stroke-width="3">
        <line x1="0" y1="130" x2="190" y2="130"/>
        <line x1="0" y1="152" x2="170" y2="152"/>
        <line x1="0" y1="174" x2="190" y2="174"/>
        <line x1="510" y1="222" x2="700" y2="222"/>
        <line x1="530" y1="244" x2="700" y2="244"/>
        <line x1="510" y1="266" x2="700" y2="266"/>
      </g>
    </svg>
    <div class="wordmark">
      <span class="wordmark__line">RW Office</span>
      <span class="wordmark__line">Partners</span>
    </div>
  </section>

  <section class="card card--back" aria-label="Business card back">
    <svg class="card__art" viewBox="0 0 700 400" aria-hidden="true">
      <path d="M0 0 H330 Q470 200 330 400 H0 Z" fill="var(--white)"/>
      <path d="M0 0 H318 Q456 200 318 400 H0 Z" fill="var(--blush-light)"/>
      <path d="M330 0 Q470 200 330 400" fill="none" stroke="var(--slate)" stroke-width="5"/>
    </svg>

    <div class="wordmark">
      <span class="wordmark__line">RW Office</span>
      <span class="wordmark__line">Partners</span>
    </div>

    <ul class="contact-list">
      <li>
        <svg class="icon" viewBox="0 0 20 20" aria-hidden="true">
          <path d="M5 2 L8 2 L9 6 L7 8 Q9 12 12 13 L14 11 L18 12 L18 15 Q18 18 15 18 Q4 16 2 5 Q2 2 5 2 Z" fill="var(--text-dark)"/>
        </svg>
        61 487 902 346
      </li>
      <li>
        <svg class="icon" viewBox="0 0 20 20" aria-hidden="true"><circle cx="10" cy="10" r="8" fill="var(--rose)"/></svg>
        @rwofficepartners
      </li>
      <li>
        <svg class="icon" viewBox="0 0 20 20" aria-hidden="true"><circle cx="10" cy="10" r="8" fill="var(--slate)"/></svg>
        @rwofficepartners
      </li>
      <li>
        <svg class="icon" viewBox="0 0 20 20" aria-hidden="true">
          <rect x="2" y="4" width="16" height="12" fill="none" stroke="var(--rose)" stroke-width="2"/>
          <path d="M2 5 L10 11 L18 5" fill="none" stroke="var(--rose)" stroke-width="2"/>
        </svg>
        marisol@rwofficepartners.com.au
      </li>
      <li>
        <svg class="icon" viewBox="0 0 20 20" aria-hidden="true">
          <g fill="none" stroke="var(--slate)" stroke-width="1.6">
            <circle cx="10" cy="10" r="8"/>
            <ellipse cx="10" cy="10" rx="3.5" ry="8"/>
            <line x1="2" y1="10" x2="18" y2="10"/>
          </g>
        </svg>
        www.rwofficepartners.com.au
      </li>
    </ul>
  </section>

</body>
</html>
```